Design a large parking banner – mandatory ticket validation in the shop

Banner Size:
548 cm (width) x 154 cm (height)
Note: The banner will be placed in a metal frame at our parking lot entrance, fully visible to every incoming truck driver. The message must be easy to read from a distance.
Goal of the Banner:
To inform all truck drivers that they must validate their entry ticket inside the shop, even if they are parking for a short time.
The message must be displayed in multiple languages for international drivers.
Mandatory Content:
Main message – in multiple languages (clearly separated or stacked):
Dutch (NL): Vergeet je ticket niet te valideren in de shop – verplicht, ook bij kort parkeren!
French (FR): N'oubliez pas de valider votre ticket à la boutique – obligatoire, même pour un court arrêt !
English (EN): Don't forget to validate your entry ticket in the shop – mandatory, even for short stops!
German (DE): Vergessen Sie nicht, Ihr Einfahrticket im Shop zu entwerten – Pflicht, auch bei kurzem Parken!
Polish (PL): Nie zapomnij zatwierdzić biletu w sklepie – obowiązkowe, nawet przy krótkim postoju!
Romanian (RO): Nu uitați să validați biletul în magazin – obligatoriu, chiar și pentru opriri scurte!
You can include more languages if space allows, but these are essential.
Opening Hours Block (in one section below):
Shop Opening Hours
Mon – Fri: 05:30 – 22:00
Sat & Sun: 08:00 – 22:00
Style & Branding:
The design must match the visual identity of Haulpoint 41Ter
Please refer to the attached photos of existing parking signage for guidance on colors, typography, and layout style
Our logo (attached) must be clearly visible and professionally integrated
Feel free to use icons or pictograms to visually support the message (e.g., ticket, truck, arrow)
Readability is key – large, bold text and high contrast colors that are visible from a distance
Target Audience:
International truck drivers – people who need fast, clear communication. Not everyone speaks the local language, so visual clarity and multilingual messaging are critical.
File Requirements:
Print-ready file (PDF or EPS) – 300 dpi at 1:10 scale
Include 5 cm bleed on all sides
Provide open source files if possible (AI or PSD)

```html
<!DOCTYPE html>
<html lang="en">
<head>
<meta charset="utf-8">
<title>Parking Banner – Ticket Validation</title>
<link rel="stylesheet" href="https://fonts.googleapis.com/css2?family=Oswald:wght@400;500;600;700&family=Roboto+Condensed:ital,wght@0,500;0,700;1,800&display=swap">
<style>
  :root {
    --page: #e9ebef;
    --navy: #2c2b5a;
    --navy-deep: #26285a;
    --navy-strip: #33336a;
    --blue: #1d7fc6;
    --blue-light: #3596d4;
    --blue-bar: #1a5fa8;
    --red: #d11f2a;
    --white: #ffffff;
  }
  * { margin: 0; padding: 0; box-sizing: border-box; }
  html, body { width: 1200px; height: 779px; overflow: hidden; background: var(--page); }
  .canvas { position: relative; width: 1200px; height: 779px; }
  .banner {
    position: absolute; left: 20px; top: 185px;
    width: 1285px; height: 453px;
    transform: scale(0.9027); transform-origin: top left;
    background: var(--navy); overflow: hidden;
    color: var(--white);
    font-family: "Oswald", "Arial Narrow", sans-serif;
  }
  .banner-shapes { position: absolute; inset: 0; }
  .headline { position: absolute; left: 33px; top: 42px; font-weight: 600; text-transform: uppercase; line-height: 1; }
  .headline-line { display: block; white-space: nowrap; }
  .headline .mark { background: var(--blue); padding: 2px 4px 4px; }
  .line-1 { font-size: 44px; }
  .line-2 { font-size: 45px; margin-top: 16px; }
  .line-3 { font-size: 62px; margin-top: 14px; }
  .line-3 .mark { padding: 2px 10px 6px 8px; }
  .hours-title { position: absolute; left: 34px; top: 252px; font-size: 42px; font-weight: 600; line-height: 61px; color: var(--navy); text-transform: uppercase; }
  .hours-list { position: absolute; left: 218px; top: 262px; font-family: "Roboto Condensed", sans-serif; font-weight: 500; font-size: 28px; line-height: 38px; }
  .hours-row { position: relative; padding-left: 47px; margin-bottom: 10px; }
  .hours-row svg { position: absolute; left: 0; top: 20px; }
  .attention-text { position: absolute; left: 616px; top: 48px; font-family: "Roboto Condensed", sans-serif; font-style: italic; font-weight: 800; font-size: 37px; line-height: 48px; text-transform: uppercase; white-space: nowrap; }
  .parking-p { position: absolute; left: 857px; top: 42px; font-size: 74px; font-weight: 500; line-height: 1; }
  .parking-divider { position: absolute; left: 918px; top: 62px; width: 2px; height: 70px; background: var(--white); }
  .parking-label { position: absolute; left: 934px; top: 54px; text-transform: uppercase; font-weight: 600; line-height: 1; }
  .parking-label .small { display: block; font-size: 26px; letter-spacing: 2px; }
  .parking-label .large { display: block; font-size: 46px; letter-spacing: 3px; margin-top: 4px; }
  .brand-name { position: absolute; left: 1058px; top: 48px; width: 210px; font-size: 40px; font-weight: 700; line-height: 46px; text-transform: uppercase; }
  .languages { position: absolute; left: 512px; top: 173px; list-style: none; font-family: "Oswald", "Arial Narrow", sans-serif; font-weight: 400; font-size: 18px; letter-spacing: -0.1px; }
  .languages li { display: flex; align-items: center; height: 43.3px; white-space: nowrap; }
  .languages svg { flex: none; margin-right: 13px; }
</style>
</head>
<body>
<div class="canvas">
  <section class="banner" aria-label="Parking banner: ticket validation required">
    <svg class="banner-shapes" width="1285" height="453" viewBox="0 0 1285 453" aria-hidden="true">
      <polygon points="710,0 1285,0 1285,453 1010,453" fill="var(--navy-deep)"/>
      <polygon points="770,453 620,230 700,230 850,453" fill="var(--navy-strip)" opacity="0.5"/>
      <polygon points="0,201 542,453 0,453" fill="var(--blue)"/>
      <polygon points="0,201 95,245 0,260" fill="var(--blue-light)"/>
      <defs>
        <linearGradient id="attention-bar" x1="0" x2="1">
          <stop offset="0" stop-color="var(--blue-bar)"/>
          <stop offset="0.55" stop-color="#1e3f86"/>
          <stop offset="1" stop-color="var(--navy-deep)"/>
        </linearGradient>
      </defs>
      <polygon points="618,45 1060,45 1060,150 598,150" fill="url(#attention-bar)"/>
      <rect x="597" y="145" width="580" height="4" fill="var(--red)"/>
    </svg>

    <h1 class="headline">
      <span class="headline-line line-1"><span class="mark">Kindly ensure</span> ticket</span>
      <span class="headline-line line-2">Validation inside the shop</span>
      <span class="headline-line line-3">Before <span class="mark">Parking</span></span>
    </h1>

    <h2 class="hours-title">Shop<br>Opening<br>Hours.</h2>
    <div class="hours-list">
      <div class="hours-row">
        <svg width="32" height="22" viewBox="0 0 32 22" aria-hidden="true"><path d="M3 2l9 9-9 9M17 2l9 9-9 9" fill="none" stroke="#fff" stroke-width="2.5"/></svg>
        Sat &amp; Sun:<br>08:00 – 22:00
      </div>
      <div class="hours-row">
        <svg width="32" height="22" viewBox="0 0 32 22" aria-hidden="true"><path d="M3 2l9 9-9 9M17 2l9 9-9 9" fill="none" stroke="#fff" stroke-width="2.5"/></svg>
        Mon – Fri:<br>05:30 – 22:00
      </div>
    </div>

    <p class="attention-text">Attention<br>Required for</p>
    <span class="parking-p">P</span>
    <span class="parking-divider"></span>
    <p class="parking-label"><span class="small">Parking</span><span class="large">Area</span></p>
    <p class="brand-name">Haulpoint<br>41Ter</p>

    <ul class="languages">
      <li lang="nl">
        <svg width="30" height="30" viewBox="0 0 30 30" aria-hidden="true"><clipPath id="f1"><circle cx="15" cy="15" r="15"/></clipPath><g clip-path="url(#f1)"><rect width="30" height="10" fill="#ae1c28"/><rect y="10" width="30" height="10" fill="#fff"/><rect y="20" width="30" height="10" fill="#21468b"/></g></svg>
        Vergeet je ticket niet te valideren in de shop – verplicht, ook bij kort parkeren!
      </li>
      <li lang="fr">
        <svg width="30" height="30" viewBox="0 0 30 30" aria-hidden="true"><clipPath id="f2"><circle cx="15" cy="15" r="15"/></clipPath><g clip-path="url(#f2)"><rect width="10" height="30" fill="#1f3fa0"/><rect x="10" width="10" height="30" fill="#fff"/><rect x="20" width="10" height="30" fill="#e1262d"/></g></svg>
        N'oubliez pas de valider votre ticket à la boutique – obligatoire, même pour un court arrêt !
      </li>
      <li lang="en">
        <svg width="30" height="30" viewBox="0 0 30 30" aria-hidden="true"><clipPath id="f3"><circle cx="15" cy="15" r="15"/></clipPath><g clip-path="url(#f3)"><rect width="30" height="30" fill="#1f2f7a"/><path d="M0 0L30 30M30 0L0 30" stroke="#fff" stroke-width="6"/><path d="M0 0L30 30M30 0L0 30" stroke="#d11f2a" stroke-width="2"/><path d="M15 0V30M0 15H30" stroke="#fff" stroke-width="8"/><path d="M15 0V30M0 15H30" stroke="#d11f2a" stroke-width="4"/></g></svg>
        Don't forget to validate your entry ticket in the shop – mandatory, even for short stops!
      </li>
      <li lang="de">
        <svg width="30" height="30" viewBox="0 0 30 30" aria-hidden="true"><clipPath id="f4"><circle cx="15" cy="15" r="15"/></clipPath><g clip-path="url(#f4)"><rect width="30" height="10" fill="#111"/><rect y="10" width="30" height="10" fill="#dd1f26"/><rect y="20" width="30" height="10" fill="#ffce00"/></g></svg>
        Vergessen Sie nicht, Ihr Einfahrticket im Shop zu entwerten – Pflicht, auch bei kurzem Parken!
      </li>
      <li lang="pl">
        <svg width="30" height="30" viewBox="0 0 30 30" aria-hidden="true"><clipPath id="f5"><circle cx="15" cy="15" r="15"/></clipPath><g clip-path="url(#f5)"><rect width="30" height="15" fill="#fff"/><rect y="15" width="30" height="15" fill="#dc143c"/></g></svg>
        Nie zapomnij zatwierdzić biletu w sklepie – obowiązkowe, nawet przy krótkim postoju!
      </li>
      <li lang="ro">
        <svg width="30" height="30" viewBox="0 0 30 30" aria-hidden="true"><clipPath id="f6"><circle cx="15" cy="15" r="15"/></clipPath><g clip-path="url(#f6)"><rect width="10" height="30" fill="#002b7f"/><rect x="10" width="10" height="30" fill="#fcd116"/><rect x="20" width="10" height="30" fill="#ce1126"/></g></svg>
        Nu uitați să validați biletul în magazin – obligatoriu, chiar și pentru opriri scurte!
      </li>
    </ul>
  </section>
</div>
</body>
</html>
```